Modern Design Business Card industrial maintenance company

Business card design for Company named Brookvale Equipment Services

Target Market(s)

Industrial

Industry/Entity Type

Maintenance and repair

Contact Information for Business Card

Place holder for address, office phone, mobile number and email

Requirements
Must have
• Clean modern look
Nice to have
• N/a

```html
<!DOCTYPE html>
<html lang="en">
<head>
<meta charset="utf-8">
<title>Brookvale Equipment Services – Business Card</title>
<link href="https://fonts.googleapis.com/css2?family=Montserrat:wght@700&family=Roboto:wght@400&display=swap" rel="stylesheet">
<style>
  :root {
    --backdrop: #d3d6d7;
    --card-white: #efeeea;
    --card-black: #1b1b1b;
    --ink: #141414;
    --ink-soft: #3a3a3a;
    --foil: #e4e4e4;
    --edge: #b8a878;
  }
  html, body {
    margin: 0;
    padding: 0;
    width: 1200px;
    height: 1050px;
    overflow: hidden;
    background: var(--backdrop);
  }
  .canvas {
    position: relative;
    width: 1200px;
    height: 1050px;
  }
  .card {
    position: absolute;
    left: 200px;
    width: 800px;
    height: 457px;
    box-sizing: border-box;
    box-shadow: 0 2px 0 var(--edge), 0 10px 24px rgba(0,0,0,0.12);
  }
  .card--front {
    top: 45px;
    background: var(--card-white);
  }
  .card--back {
    top: 548px;
    background: var(--card-black);
  }

  /* front */
  .brand-mark {
    position: absolute;
    left: 62px;
    top: 58px;
    display: flex;
    align-items: center;
    gap: 18px;
    font-family: "Roboto", sans-serif;
    font-size: 17px;
    letter-spacing: 3px;
    text-transform: uppercase;
    color: var(--ink);
  }
  .brand-mark__circle {
    width: 96px;
    height: 96px;
    border: 6px solid var(--ink);
    border-radius: 50%;
    box-sizing: border-box;
  }
  .contact {
    position: absolute;
    right: 56px;
    top: 168px;
    text-align: right;
    font-family: "Roboto", sans-serif;
    color: var(--ink-soft);
    font-size: 19px;
    line-height: 1.28;
  }
  .contact__name {
    font-family: "Montserrat", sans-serif;
    font-weight: 700;
    font-size: 25px;
    letter-spacing: 0.5px;
    color: var(--ink);
    margin: 0;
  }
  .contact__title {
    margin: 0 0 10px;
    font-size: 19px;
  }
  .contact__address {
    margin: 0 0 12px;
    font-style: normal;
  }
  .contact__list {
    list-style: none;
    margin: 0;
    padding: 0;
  }
  .contact__list li {
    display: flex;
    justify-content: flex-end;
    align-items: center;
    gap: 10px;
  }
  .contact__icon {
    width: 18px;
    height: 18px;
    flex: none;
  }

  /* back */
  .back-brand {
    position: absolute;
    inset: 0;
    display: flex;
    flex-direction: column;
    align-items: center;
    justify-content: center;
    gap: 26px;
  }
  .back-brand__circle {
    width: 150px;
    height: 150px;
    border: 7px solid var(--foil);
    border-radius: 50%;
    box-sizing: border-box;
  }
  .back-brand__name {
    font-family: "Roboto", sans-serif;
    font-size: 30px;
    letter-spacing: 6px;
    text-transform: uppercase;
    color: var(--foil);
    margin: 0;
  }
</style>
</head>
<body>
<main class="canvas">
  <section class="card card--front" aria-label="Business card front">
    <div class="brand-mark">
      <span class="brand-mark__circle" aria-hidden="true"></span>
      <span class="brand-mark__name">Brookvale Equipment Services</span>
    </div>

    <div class="contact">
      <p class="contact__name">DANIEL HARTWELL</p>
      <p class="contact__title">Managing Director</p>
      <address class="contact__address">
        Brookvale Equipment Services<br>
        118 W Harlow St<br>
        Riverton, CA 93310
      </address>
      <ul class="contact__list">
        <li>(555) 214-7390
          <svg class="contact__icon" viewBox="0 0 24 24" aria-hidden="true"><circle cx="12" cy="12" r="12" fill="#141414"/><path d="M7 9c0-2 2-3 5-3s5 1 5 3l-2 1-1-1H10L9 10z M8 18l1-6h6l1 6z" fill="#efeeea"/><circle cx="12" cy="14.5" r="1.6" fill="#141414"/></svg>
        </li>
        <li>info@brookvaleequip.com
          <svg class="contact__icon" viewBox="0 0 24 24" aria-hidden="true"><rect x="1" y="5" width="22" height="14" rx="2" fill="#141414"/><path d="M2 6l10 7 10-7" fill="none" stroke="#efeeea" stroke-width="1.6"/></svg>
        </li>
        <li>www.brookvaleequip.com
          <svg class="contact__icon" viewBox="0 0 24 24" aria-hidden="true"><circle cx="12" cy="12" r="11" fill="#141414"/><g fill="none" stroke="#efeeea" stroke-width="1.4"><ellipse cx="12" cy="12" rx="4.5" ry="10"/><path d="M2 12h20M4 7h16M4 17h16"/></g></svg>
        </li>
      </ul>
    </div>
  </section>

  <section class="card card--back" aria-label="Business card back">
    <div class="back-brand">
      <span class="back-brand__circle" aria-hidden="true"></span>
      <p class="back-brand__name">Brookvale Equipment Services</p>
    </div>
  </section>
</main>
</body>
</html>
```